Copper Gavel Auctions business card design with existing logo

Looking for a sleek and sexy design using our current logo

Contact Information for Business Card

Name, address, email, phone, website. Marcus Delvane 418 Birchmont Road Suite 200C Fenwick NY 11093 Copperbidhouse.net (631)582-4067

```html
<!DOCTYPE html>
<html lang="en">
<head>
<meta charset="utf-8">
<title>Copper Gavel Auctions – Business Card</title>
<link rel="stylesheet" href="https://fonts.googleapis.com/css2?family=Open+Sans:wght@400;700&display=swap">
<style>
  :root {
    --backdrop: #cdcdcf;
    --card: #ffffff;
    --brand-red: #d32029;
    --brand-navy: #1d3f7d;
    --ink-light: #ffffff;
  }
  * { margin: 0; padding: 0; box-sizing: border-box; }
  html, body {
    width: 1200px; height: 1000px; overflow: hidden;
    background: var(--backdrop);
    font-family: "Open Sans", sans-serif;
  }
  .canvas { position: relative; width: 1200px; height: 1000px; }
  .card {
    position: absolute; left: 372px; width: 480px; height: 283px;
    background: var(--card); border-radius: 18px; overflow: hidden;
  }
  .card--front { top: 172px; }
  .card--back { top: 550px; }

  .brand {
    position: absolute; display: flex; flex-direction: column; align-items: center;
    transform: translate(-50%, -50%);
  }
  .brand__dot {
    width: 34px; height: 34px; border-radius: 50%;
    background: var(--brand-navy); margin-bottom: 8px;
  }
  .brand__name {
    font-weight: 700; color: var(--brand-red);
    font-size: 17px; line-height: 1.15; text-align: center; letter-spacing: 0.5px;
  }
  .card--front .brand { left: 240px; top: 140px; }
  .card--back .brand { left: 362px; top: 134px; }

  .contact-panel {
    position: absolute; left: 0; top: 0; width: 240px; height: 100%;
    background: var(--brand-red); color: var(--ink-light);
  }
  .contact-panel__name {
    position: absolute; left: 45px; top: 80px;
    font-size: 18px; font-weight: 400;
  }
  .contact-list { position: absolute; left: 45px; top: 117px; list-style: none; }
  .contact-list__item {
    display: flex; align-items: flex-start; gap: 7px;
    font-size: 12.3px; line-height: 14px; margin-bottom: 7.8px;
  }
  .contact-list__icon {
    flex: none; width: 14px; height: 14px; background: var(--ink-light);
    border-radius: 2px; display: flex; align-items: center; justify-content: center;
  }
  .contact-list__address { line-height: 22px; margin-top: -4px; }
  .contact-list__address span { display: block; padding-left: 3px; }

  .social { position: absolute; left: 382px; top: 246px; display: flex; gap: 4px; }
  .social__dot { width: 14.5px; height: 14.5px; border-radius: 50%; background: var(--brand-navy); }
</style>
</head>
<body>
<main class="canvas">
  <section class="card card--front">
    <div class="brand">
      <div class="brand__dot"></div>
      <div class="brand__name">Copper Gavel<br>Auctions</div>
    </div>
  </section>

  <section class="card card--back">
    <div class="contact-panel">
      <h1 class="contact-panel__name">Marcus Delvane</h1>
      <ul class="contact-list">
        <li class="contact-list__item">
          <span class="contact-list__icon"><svg width="10" height="10" viewBox="0 0 10 10"><path d="M2 1 L4 1 L4.5 3 L3.3 3.8 Q4.3 6 6.2 6.7 L7 5.5 L9 6 L9 8 Q8.5 9 7.5 9 Q2 8 1 2.5 Q1 1.5 2 1Z" fill="#d32029"/></svg></span>
          (631)582-4067
        </li>
        <li class="contact-list__item">
          <span class="contact-list__icon"><svg width="10" height="8" viewBox="0 0 10 8"><rect x="0.5" y="0.5" width="9" height="7" fill="none" stroke="#d32029"/><path d="M0.5 0.8 L5 4.5 L9.5 0.8" fill="none" stroke="#d32029"/></svg></span>
          youremail@mailbox.com
        </li>
        <li class="contact-list__item">
          <span class="contact-list__icon"><svg width="10" height="10" viewBox="0 0 10 10" fill="none" stroke="#d32029" stroke-width="0.8"><circle cx="5" cy="5" r="4.3"/><ellipse cx="5" cy="5" rx="2" ry="4.3"/><path d="M0.7 5 H9.3 M1.5 2.8 H8.5 M1.5 7.2 H8.5"/></svg></span>
          Copperbidhouse.net
        </li>
        <li class="contact-list__item">
          <span class="contact-list__icon"><svg width="8" height="11" viewBox="0 0 8 11"><path d="M4 11 Q0 6 0 4 A4 4 0 0 1 8 4 Q8 6 4 11Z" fill="#d32029"/><circle cx="4" cy="4" r="1.5" fill="#fff"/></svg></span>
          <span class="contact-list__address">418 Birchmont Road Suite<span>200C Fenwick NY 11093</span></span>
        </li>
      </ul>
    </div>

    <div class="brand">
      <div class="brand__dot"></div>
      <div class="brand__name">Copper Gavel<br>Auctions</div>
    </div>

    <div class="social" aria-label="Social links">
      <span class="social__dot"></span><span class="social__dot"></span><span class="social__dot"></span><span class="social__dot"></span>
    </div>
  </section>
</main>
</body>
</html>
```